Dorrington Thermal Heating and Air Conditioning web page

This is a repair, installation and maintenance residential company. I don't do commercial. I need a web design that shows a company with 24/7 fast service that is easy for customers to contact me from. I am a Brackley /Velmora HVAC dealer and their logos can be on there also. I also sell IAQ products like Zenta- Orbit and I offer duct cleanings as well.

Industry/Entity Type

Hvac

Coding

Coded - Design and coding required

Number of Pages Required

2 page

```html
<!DOCTYPE html>
<html lang="en">
<head>
<meta charset="utf-8">
<title>Dorrington Thermal Heating and Air Conditioning</title>
<link rel="stylesheet" href="https://fonts.googleapis.com/css2?family=Rajdhani:wght@500;600;700&family=Roboto:wght@400;500&display=swap">
<style>
:root{
  --red:#d9121b;
  --red-dark:#c20f17;
  --blue:#00a8ec;
  --ink:#1d1d1d;
  --text:#555;
  --muted:#6b6b6b;
  --footer:#1c1c1c;
  --white:#fff;
}
*{box-sizing:border-box;margin:0;padding:0}
html,body{width:1200px;height:2992px;overflow:hidden}
body{position:relative;background:var(--white);font-family:"Roboto",sans-serif;color:var(--text)}
.abs{position:absolute}

.top-rule{left:0;top:0;width:1200px;height:5px;background:var(--red)}
.brand{left:110px;top:24px;font-family:"Rajdhani",sans-serif;font-weight:700;font-size:25px;line-height:24px;color:var(--ink);letter-spacing:.5px}
.callus{right:112px;top:28px;display:flex;align-items:center;gap:10px;font-family:"Rajdhani",sans-serif;font-weight:500;font-size:19px;color:#333}
.callus .ring{width:34px;height:34px;border-radius:50%;background:var(--red);display:flex;align-items:center;justify-content:center}

.nav{left:110px;top:89px;width:760px;height:48px;background:var(--blue);display:flex;align-items:center;font-family:"Rajdhani",sans-serif;font-weight:700;font-size:14px;color:var(--white)}
.nav a{color:inherit;text-decoration:none;height:100%;display:flex;align-items:center;justify-content:center}
.nav .home{background:var(--red);width:120px}
.nav .sep{width:1px;height:18px;background:rgba(255,255,255,.35)}
.quote-tab{left:848px;top:89px;width:240px;height:48px}
.quote-tab span{position:absolute;left:52px;top:13px;font-family:"Rajdhani",sans-serif;font-weight:600;font-size:19px;color:var(--white)}

.hero{left:0;top:121px;width:1200px;height:609px;z-index:-1}
.hero-card{left:110px;top:302px;width:340px;height:209px;background:rgba(40,40,40,.78);padding:26px 23px;color:var(--white)}
.hero-card .kicker{font-family:"Rajdhani",sans-serif;font-weight:600;font-size:19px;white-space:nowrap}
.hero-card h1{font-family:"Rajdhani",sans-serif;font-weight:600;font-size:22px;margin-top:4px;letter-spacing:.2px;white-space:nowrap}
.hero-card p{font-size:12px;line-height:24px;margin-top:10px;white-space:nowrap}
.btn{display:inline-block;background:var(--red);color:var(--white);font-family:"Rajdhani",sans-serif;font-weight:700;font-size:13px;letter-spacing:.3px}
.hero-card .btn{margin-top:8px;padding:7px 10px}

.quote-form{left:810px;top:137px;width:278px;height:386px;background:var(--red);padding:26px 20px}
.field{height:33px;border:1px solid rgba(255,255,255,.85);margin-bottom:8px;color:var(--white);font-size:11px;padding:10px 11px;position:relative}
.field.area{height:75px;margin-bottom:13px}
.field .caret{position:absolute;right:10px;top:12px;width:0;height:0;border-left:4px solid transparent;border-right:4px solid transparent;border-top:7px solid var(--white)}
.submit{height:32px;background:var(--blue);color:var(--white);font-family:"Rajdhani",sans-serif;font-weight:700;font-size:14px;display:flex;align-items:center;justify-content:center}

.section-title{left:0;width:1200px;text-align:center;font-family:"Rajdhani",sans-serif;font-weight:600;font-size:32px;color:var(--ink);letter-spacing:.3px}
.section-title em{font-style:normal;color:var(--red)}
.section-sub{left:0;width:1200px;text-align:center;font-size:12px;color:var(--text)}

.service{width:260px;text-align:center}
.service svg{display:block;margin:0 auto}
.service h3{font-family:"Rajdhani",sans-serif;font-weight:700;font-size:18px;margin-top:10px;letter-spacing:.4px}
.service p{font-size:12px;line-height:21.5px;color:var(--muted);margin-top:4px}

.about-bg{left:0;top:1151px;width:1200px;height:425px}
.about-copy{left:634px;top:1192px;width:455px;color:var(--white)}
.about-copy h2{font-family:"Rajdhani",sans-serif;font-weight:600;font-size:54px;line-height:60px}
.about-copy h4{font-family:"Rajdhani",sans-serif;font-weight:500;font-size:19px;margin-top:8px;letter-spacing:.3px;white-space:nowrap}
.about-copy p{font-size:12.5px;line-height:25.8px;margin-top:22px;text-align:justify}
.about-copy .btn{margin-top:36px;padding:12px 19px}

.post{width:313px;height:399px;background:var(--white);box-shadow:0 2px 8px rgba(0,0,0,.12)}
.post .thumb{display:block;width:313px;height:214px}
.post .meta{padding:24px 16px 0;font-family:"Rajdhani",sans-serif;font-weight:500;font-size:15px;color:var(--blue)}
.post .meta i{font-style:normal;margin:0 18px;color:#9cc}
.post h5{padding:10px 16px 0;font-family:"Rajdhani",sans-serif;font-weight:500;font-size:21px;line-height:30px;color:#333}
.post .foot{position:absolute;left:0;bottom:0;width:100%;height:47px;border-top:1px solid #e6e6e6;display:flex;align-items:center;justify-content:space-between;padding:0 11px 0 15px;font-family:"Rajdhani",sans-serif;font-weight:700;font-size:14px;color:var(--blue)}

.testimonials{left:0;top:2174px;width:1200px;height:454px}
.testi-title{left:110px;top:2276px;font-family:"Rajdhani",sans-serif;font-weight:600;font-size:32px;color:var(--ink)}
.testi-title em{font-style:normal;color:var(--blue)}
.testi-quote{left:110px;top:2355px}
.testi-text{left:148px;top:2356px;width:385px;font-size:12.5px;line-height:24.2px;text-align:justify;color:#555}
.testi-author{left:148px;top:2494px;font-family:"Rajdhani",sans-serif;font-weight:600;font-size:15px;color:#333}
.testi-author small{font-family:"Roboto",sans-serif;font-weight:400;font-size:10px;color:#777}

.footer{left:0;top:2628px;width:1200px;height:364px;background:var(--footer)}
.dealers{left:0;top:2681px;width:1200px;display:flex;justify-content:center;gap:40px;font-family:"Rajdhani",sans-serif;font-weight:700;font-size:40px;color:var(--white)}
.foot-nav{left:0;top:2783px;width:1200px;display:flex;justify-content:center;gap:55px;font-size:11.5px;color:var(--white)}
.socials{left:390px;top:2834px;display:flex;gap:12px}
.socials span{width:60px;height:60px;border:1.5px solid rgba(255,255,255,.85);border-radius:50%;display:flex;align-items:center;justify-content:center}
.socials span b{width:6px;height:6px;border-radius:50%;background:var(--white)}
.copyright{left:0;top:2926px;width:1200px;text-align:center;font-size:14px;color:var(--white)}
</style>
</head>
<body>

<div class="abs top-rule"></div>

<div class="abs brand">DORRINGTON<br>THERMAL</div>

<div class="abs callus">
  <span class="ring">
    <svg width="18" height="18" viewBox="0 0 24 24" aria-hidden="true"><path d="M6.6 10.8a15 15 0 0 0 6.6 6.6l2.2-2.2a1 1 0 0 1 1-.25 11.4 11.4 0 0 0 3.6.57 1 1 0 0 1 1 1V20a1 1 0 0 1-1 1A17 17 0 0 1 3 4a1 1 0 0 1 1-1h3.5a1 1 0 0 1 1 1c0 1.25.2 2.45.57 3.6a1 1 0 0 1-.25 1z" fill="none" stroke="#fff" stroke-width="1.6"/></svg>
  </span>
  Call us : 000-555-0148
</div>

<svg class="abs hero" viewBox="0 0 1200 609" role="img" aria-label="Photo of a woman relaxing on a sofa under a wall air conditioner in a bright living room">
  <defs>
    <linearGradient id="heroTone" x1="0" y1="0" x2="1" y2="1">
      <stop offset="0" stop-color="#c9c4bd"/>
      <stop offset=".5" stop-color="#aaa49c"/>
      <stop offset="1" stop-color="#8c8782"/>
    </linearGradient>
  </defs>
  <path d="M0,0 H1200 V529 Q600,689 0,529 Z" fill="url(#heroTone)"/>
</svg>

<nav class="abs nav">
  <a class="home" href="#">HOME</a>
  <a href="#" style="width:108px">ABOUT US</a><span class="sep"></span>
  <a href="#" style="width:112px">SERVICES</a><span class="sep"></span>
  <a href="#" style="width:96px">NEWS</a><span class="sep"></span>
  <a href="#" style="width:112px">GALLERY</a><span class="sep"></span>
  <a href="#" style="width:128px">CONTACT US</a>
</nav>

<div class="abs quote-tab">
  <svg width="240" height="48" viewBox="0 0 240 48" aria-hidden="true"><path d="M34,0 H240 V48 H0 Z" fill="var(--red)"/></svg>
  <span>REQUEST A QUOTE</span>
</div>

<form class="abs quote-form">
  <div class="field">Name :</div>
  <div class="field">Email :</div>
  <div class="field">Phone :</div>
  <div class="field">Services :<span class="caret"></span></div>
  <div class="field">dd/mm/yyyy :</div>
  <div class="field area">Comments :</div>
  <div class="submit">SUBMIT</div>
</form>

<div class="abs hero-card">
  <div class="kicker">DORRINGTON THERMAL</div>
  <h1>HEATING AND AIR CONDITIONING</h1>
  <p>Sed ut perspiciatis unde omnis iste natus error sit volu<br>ptatem&nbsp; beatae vitae dicta sunt explicabo.</p>
  <span class="btn">READ MORE</span>
</div>

<h2 class="abs section-title" style="top:784px">OUR <em>SERVICES</em></h2>
<p class="abs section-sub" style="top:830px">Sed ut perspiciatis unde omnis iste natus error sit voluptatem accusantium doloremque laudantium</p>

<div class="abs service" style="left:138px;top:888px">
  <svg width="108" height="108" viewBox="0 0 108 108" aria-hidden="true">
    <circle cx="54" cy="54" r="52" fill="var(--red)"/><circle cx="54" cy="54" r="45" fill="none" stroke="#fff" stroke-width="2.5"/>
    <path d="M38 70 L62 46 M66 36 a8 8 0 1 1 6 6 M40 40 L70 70" stroke="#fff" stroke-width="7" stroke-linecap="round" fill="none"/>
  </svg>
  <h3 style="color:var(--red)">REPAIR</h3>
  <p>Sed ut perspiciatis unde omnis iste<br>natus error sit voluptatem accusantium<br>doloremque laudantium</p>
</div>

<div class="abs service" style="left:469px;top:888px">
  <svg width="108" height="108" viewBox="0 0 108 108" aria-hidden="true">
    <circle cx="54" cy="54" r="52" fill="var(--blue)"/><circle cx="54" cy="54" r="45" fill="none" stroke="#fff" stroke-width="2.5"/>
    <rect x="30" y="36" width="48" height="20" rx="3" fill="none" stroke="#fff" stroke-width="4"/>
    <path d="M36 46 H72 M40 64 q-3 6 0 12 M54 64 q-3 6 0 12 M68 64 q-3 6 0 12" stroke="#fff" stroke-width="3.5" fill="none" stroke-linecap="round"/>
  </svg>
  <h3 style="color:var(--blue)">INSTALLATION</h3>
  <p>Sed ut perspiciatis unde omnis iste<br>natus error sit voluptatem accusantium<br>doloremque laudantium</p>
</div>

<div class="abs service" style="left:812px;top:888px">
  <svg width="108" height="108" viewBox="0 0 108 108" aria-hidden="true">
    <circle cx="54" cy="54" r="52" fill="var(--red)"/><circle cx="54" cy="54" r="45" fill="none" stroke="#fff" stroke-width="2.5"/>
    <rect x="28" y="36" width="52" height="36" rx="3" fill="none" stroke="#fff" stroke-width="3.5"/>
    <circle cx="46" cy="54" r="11" fill="none" stroke="#fff" stroke-width="3.5"/>
    <path d="M64 44 H74 M64 52 H74 M64 60 H74" stroke="#fff" stroke-width="3"/>
  </svg>
  <h3 style="color:var(--red)">MAINTENANCE</h3>
  <p>Sed ut perspiciatis unde omnis iste<br>natus error sit voluptatem accusantium<br>doloremque laudantium</p>
</div>

<svg class="abs about-bg" viewBox="0 0 1200 425" aria-hidden="true">
  <defs>
    <radialGradient id="aboutGrey" cx=".25" cy=".5" r=".6">
      <stop offset="0" stop-color="#e6e6e6"/><stop offset="1" stop-color="#9f9f9f"/>
    </radialGradient>
  </defs>
  <rect width="1200" height="425" fill="url(#aboutGrey)"/>
  <path d="M526,0 Q682,212 526,425 H1200 V0 Z" fill="var(--blue)"/>
</svg>
<div class="abs" role="img" aria-label="Photo of the company service pickup truck with a 24/7 emergency service badge" style="left:0;top:1200px;width:590px;height:310px;background:linear-gradient(180deg,rgba(60,60,60,0) 0%,rgba(45,45,45,.55) 45%,rgba(35,35,35,.7) 75%,rgba(60,60,60,0) 100%)"></div>

<div class="abs about-copy">
  <h2>ABOUT</h2>
  <h4>DORRINGTON THERMAL HEATING &amp; AIR CONDITIONING</h4>
  <p>Sed ut perspiciatis unde omnis iste natus error sit voluptatem accusantium dol oremque laudantium, totam rem aperiam, eaque ipsa quae ab illo inventore veritatis et quasi architecto beatae vitae dicta sunt explicabo. Nemo enim ipsam voluptatem quia voluptas sit aspernatur aut odit aut fugit, magni dolores eos qui ratione voluptatem sequi nesciunt</p>
  <span class="btn">READ MORE</span>
</div>

<h2 class="abs section-title" style="top:1614px">LATEST <em>BLOG</em></h2>
<p class="abs section-sub" style="top:1661px">Sed ut perspiciatis unde omnis iste natus error sit voluptatem accusantium doloremque laudantium</p>

<article class="abs post" style="left:110px;top:1703px">
  <div class="thumb" role="img" aria-label="Photo of a hand pointing a remote at an air conditioner" style="background:linear-gradient(135deg,#d9d2cc,#efe9e4 55%,#c7bdb4)"></div>
  <div class="meta">15 APRIL 2020<i>|</i>COMMENTS</div>
  <h5>Sed ut perspiciatis unde omnis natus error sit voluptatem</h5>
  <div class="foot">READ MORE <svg width="18" height="18" viewBox="0 0 18 18" aria-hidden="true"><circle cx="9" cy="9" r="9" fill="var(--blue)"/><path d="M5 9 H12 M9 5.5 L12.5 9 L9 12.5" stroke="#fff" stroke-width="2" fill="none"/></svg></div>
</article>

<article class="abs post" style="left:442px;top:1703px">
  <div class="thumb" role="img" aria-label="Photo of a technician checking an outdoor condenser unit with gauges" style="background:linear-gradient(135deg,#b8c0c6,#8d9aa5 50%,#3e5a7a)"></div>
  <div class="meta">15 APRIL 2020<i>|</i>COMMENTS</div>
  <h5>Sed ut perspiciatis unde omnis natus error sit voluptatem</h5>
  <div class="foot">READ MORE <svg width="18" height="18" viewBox="0 0 18 18" aria-hidden="true"><circle cx="9" cy="9" r="9" fill="var(--blue)"/><path d="M5 9 H12 M9 5.5 L12.5 9 L9 12.5" stroke="#fff" stroke-width="2" fill="none"/></svg></div>
</article>

<article class="abs post" style="left:774px;top:1703px">
  <div class="thumb" role="img" aria-label="Photo of a woman adjusting a wall thermostat" style="background:linear-gradient(135deg,#e3e1dc,#c9ccc9 50%,#51708f)"></div>
  <div class="meta">15 APRIL 2020<i>|</i>COMMENTS</div>
  <h5>Sed ut perspiciatis unde omnis natus error sit voluptatem</h5>
  <div class="foot">READ MORE <svg width="18" height="18" viewBox="0 0 18 18" aria-hidden="true"><circle cx="9" cy="9" r="9" fill="var(--blue)"/><path d="M5 9 H12 M9 5.5 L12.5 9 L9 12.5" stroke="#fff" stroke-width="2" fill="none"/></svg></div>
</article>

<div class="abs testimonials" role="img" aria-label="Photo of a woman pointing a remote at a wall air conditioner in a bright room" style="background:linear-gradient(90deg,#eaf3f8 0%,#f3f7f9 40%,#e6edf2 60%,#c9d6e0 85%,#eef2f5 100%)"></div>
<h2 class="abs testi-title">CLIENT <em>TESTIMONIALS</em></h2>
<svg class="abs testi-quote" width="28" height="24" viewBox="0 0 28 24" aria-hidden="true"><path d="M0 24 V13 Q0 3 11 0 L12 4 Q6 6 6 11 H12 V24 Z M15 24 V13 Q15 3 26 0 L27 4 Q21 6 21 11 H27 V24 Z" fill="var(--blue)"/></svg>
<p class="abs testi-text">Sed ut perspiciatis unde omnis iste natus error sit voluptatem accusantium doloremque laudantium, totam rem aperiam, eaque ipsa quae ab illo inventore veritatis et quasi architecto beatae vitae dicta sunt explicabo. Nemo enim ipsam voluptatem quia voluptas sit eos qui ratione voluptatem sequi nesciunt.</p>
<p class="abs testi-author">-Clara Penfold <small>posted on 15 April 2020</small></p>

<footer class="abs footer"></footer>
<div class="abs dealers"><span>Brackley</span><span>Velmora</span></div>
<nav class="abs foot-nav"><span>HOME</span><span>ABOUT US</span><span>SERVICES</span><span>BLOG</span><span>GALLERY</span><span>CONTACT US</span></nav>
<div class="abs socials">
  <span aria-label="Social profile"><b></b></span>
  <span aria-label="Social profile"><b></b></span>
  <span aria-label="Social profile"><b></b></span>
  <span aria-label="Social profile"><b></b></span>
  <span aria-label="Social profile"><b></b></span>
  <span aria-label="Email"><svg width="18" height="14" viewBox="0 0 18 14" aria-hidden="true"><rect x="1" y="1" width="16" height="12" rx="1.5" fill="none" stroke="#fff" stroke-width="1.5"/><path d="M1.5 2 L9 8 L16.5 2" fill="none" stroke="#fff" stroke-width="1.5"/></svg></span>
</div>
<p class="abs copyright">© Copyrights 2020-Dorrington Thermal Heating and Air Conditioning.All Rights Reserved.</p>

</body>
</html>
```